UI design for kiosk touch screen

We need a UI design for a touch screen device to be used by costumers in a store and show information about specific products. We're looking for a general concept to serve as a starting point and we're not expecting a fully coded design.
We envision a UI where it first shows a range of products; once touched, it should show information about the product which includes text, touchable photos, videos and document files. We're interested in the starting page and the product details page.
We are the suppliers of the device and not the owners of stores that will use them. The purpose of this design is for in-person demonstrations to potential clients or in ads so the design should be agnostic about the end product(s). You may freely pick random placeholder or fictional products and assets to showcase the design concept as long as they can be changed without compromising the design. You can use our logo (annexed) in the design as a placeholder but it's not necessary.
We're using web technologies to develop the UI so the same principles should apply, except some exceptions below:
- There's no need for a responsive design since the resolution is set at 1920x1080 on a 22'' monitor in landscape orientation.
- All interactions will be done using the touchscreen, so any interactive component needs to be large enough for navigation to be comfortable.
- The design should be visually engaging and eye-catching, more so than a regular website.
Physical shop owners.
Store
2 page

```html
<!DOCTYPE html>
<html lang="en">
<head>
<meta charset="utf-8">
<title>Kiosk – Mobile Phones</title>
<link href="https://fonts.googleapis.com/css2?family=Open+Sans:wght@400;500;600;700&display=swap" rel="stylesheet">
<style>
  :root{
    --blue:#1e88f0;
    --blue-text:#1f86e6;
    --orange:#f7901e;
    --white:#ffffff;
    --ink:#1d1d1d;
    --grey:#e3e3e3;
  }
  *{margin:0;padding:0;box-sizing:border-box}
  html,body{width:1200px;height:674px;overflow:hidden;background:#fff;font-family:"Open Sans",sans-serif}
  .kiosk{position:relative;width:1200px;height:674px;background:var(--white);overflow:hidden}

  .brand{position:absolute;left:34px;top:24px;display:flex;align-items:center;gap:8px}
  .brand-square{width:24px;height:24px;background:var(--blue)}
  .brand-name{font-size:25px;font-weight:700;color:var(--blue);letter-spacing:.3px}

  .page-title{position:absolute;left:306px;top:26px;width:348px;display:flex;align-items:center;gap:12px}
  .page-title .rule{flex:1;height:2px;background:var(--orange)}
  .page-title h1{font-size:21px;font-weight:400;color:var(--blue-text);white-space:nowrap}

  .call{position:absolute;left:846px;top:18px;display:flex;align-items:center;gap:12px}
  .call-icon{width:41px;height:41px;border-radius:50%;background:var(--grey);display:flex;align-items:center;justify-content:center}
  .call-label{font-size:18px;color:var(--orange);line-height:1.1}
  .call-number{font-size:22px;font-weight:600;color:var(--blue-text);line-height:1.2}

  .sidebar{position:absolute;left:0;top:80px;width:127px;height:557px;background:var(--blue);box-shadow:3px 0 5px rgba(0,0,0,.25)}
  .nav-item{height:94px;display:flex;flex-direction:column;align-items:center;justify-content:center;gap:6px;color:var(--white);font-size:16px;border-bottom:1px solid rgba(255,255,255,.35)}
  .nav-item:last-child{border-bottom:none}

  .product-grid{position:absolute;left:170px;top:80px}
  .product{position:absolute;width:188px}
  .product-photo{width:188px;height:128px;border:2px solid #3f95ea;background:linear-gradient(180deg,#fafafa,#e9ebee);display:flex;align-items:center;justify-content:center}
  .product-photo span{display:block;width:70px;height:112px;border-radius:6px;background:linear-gradient(180deg,#d8d8d8 0 18%,#f4f4f4 18% 100%)}
  .product-name{margin-top:4px;text-align:center;font-size:13px;font-weight:500;color:var(--ink)}

  .btn{position:absolute;top:579px;width:130px;height:43px;display:flex;align-items:center;justify-content:center;gap:12px;color:var(--white);font-size:22px}
  .btn-back{left:198px;background:var(--orange)}
  .btn-main{left:414px;background:var(--blue)}
  .btn-next{left:630px;background:var(--orange)}

  .panel{position:absolute;left:844px;top:80px;width:356px;height:557px;background:var(--orange)}
  .panel-heading{position:absolute;left:29px;width:299px;display:flex;align-items:center;gap:10px}
  .panel-heading .rule{flex:1;height:1px;background:#c86f10}
  .panel-heading h2{font-size:19px;font-weight:400;color:var(--blue-text)}
  .select{position:absolute;left:23px;width:309px;height:54px;background:linear-gradient(90deg,#fff 45%,#e4e4e4);display:flex;align-items:center;justify-content:space-between;padding:0 18px 0 14px;font-size:18px;color:var(--blue-text)}
  .category{position:absolute;width:89px;height:89px;background:var(--white);display:flex;flex-direction:column;align-items:center;justify-content:center;gap:6px;font-size:12px;line-height:1.05;color:#3a92ea;text-align:center}

  .footer{position:absolute;left:0;top:637px;width:1200px;height:37px;background:linear-gradient(180deg,#e8e8e8,#fafafa);display:flex;align-items:center;justify-content:space-between;padding:0 44px 0 50px;font-size:16px;color:var(--ink)}
</style>
</head>
<body>
<div class="kiosk">

  <div class="brand"><span class="brand-square"></span><span class="brand-name">Kalvetrix</span></div>

  <div class="page-title"><span class="rule"></span><h1>Mobile Phones</h1><span class="rule"></span></div>

  <div class="call">
    <div class="call-icon">
      <svg width="16" height="16" viewBox="0 0 24 24"><path fill="#f7901e" d="M6.6 10.8a15.1 15.1 0 0 0 6.6 6.6l2.2-2.2c.3-.3.7-.4 1-.2 1.1.4 2.3.6 3.6.6.6 0 1 .4 1 1V20c0 .6-.4 1-1 1A17 17 0 0 1 3 4c0-.6.4-1 1-1h3.5c.6 0 1 .4 1 1 0 1.3.2 2.5.6 3.6.1.3 0 .7-.2 1z"/></svg>
    </div>
    <div><div class="call-label">Call Us</div><div class="call-number">123 456 7890</div></div>
  </div>

  <nav class="sidebar">
    <div class="nav-item">
      <svg width="22" height="20" viewBox="0 0 24 22"><path fill="#fff" d="M12 2 1 11h3v10h6v-6h4v6h6V11h3z"/></svg>Home</div>
    <div class="nav-item">
      <svg width="22" height="22" viewBox="0 0 24 24" stroke="#fff" stroke-width="2" fill="none"><path d="M12 2v20M3.3 7l17.4 10M3.3 17 20.7 7M9 3l3 3 3-3M9 21l3-3 3 3"/></svg>New</div>
    <div class="nav-item">
      <svg width="24" height="20" viewBox="0 0 24 20"><path fill="#fff" d="M8 2h8v3h-2V4h-4v1H8zM1 6h22v13H1z"/><path stroke="#1e88f0" stroke-width="1.5" d="M6 6v13M18 6v13"/></svg>About</div>
    <div class="nav-item">
      <svg width="20" height="20" viewBox="0 0 24 24"><path fill="#fff" d="M6.6 10.8a15.1 15.1 0 0 0 6.6 6.6l2.2-2.2c.3-.3.7-.4 1-.2 1.1.4 2.3.6 3.6.6.6 0 1 .4 1 1V20c0 .6-.4 1-1 1A17 17 0 0 1 3 4c0-.6.4-1 1-1h3.5c.6 0 1 .4 1 1 0 1.3.2 2.5.6 3.6.1.3 0 .7-.2 1z"/></svg>Contact</div>
    <div class="nav-item">
      <svg width="22" height="22" viewBox="0 0 24 24"><circle cx="12" cy="12" r="10" fill="none" stroke="#fff" stroke-width="2"/><path d="M9 9.5a3 3 0 1 1 4 2.8c-.7.3-1 .8-1 1.5V15" fill="none" stroke="#fff" stroke-width="2"/><circle cx="12" cy="18" r="1.3" fill="#fff"/></svg>Help</div>
  </nav>

  <section class="product-grid">
    <div class="product" style="left:0;top:0"><div class="product-photo" role="img" aria-label="Product photo: white touch-screen kiosk"><span></span></div><p class="product-name">Nulla profecto est</p></div>
    <div class="product" style="left:216px;top:0"><div class="product-photo" role="img" aria-label="Product photo: white touch-screen kiosk"><span></span></div><p class="product-name">Primo ad extremum</p></div>
    <div class="product" style="left:436px;top:0"><div class="product-photo" role="img" aria-label="Product photo: white touch-screen kiosk"><span></span></div><p class="product-name">Neque enim civitas</p></div>
    <div class="product" style="left:0;top:166px"><div class="product-photo" role="img" aria-label="Product photo: white touch-screen kiosk"><span></span></div><p class="product-name">Similitudines eas</p></div>
    <div class="product" style="left:216px;top:166px"><div class="product-photo" role="img" aria-label="Product photo: white touch-screen kiosk"><span></span></div><p class="product-name">Nullum inveniri</p></div>
    <div class="product" style="left:436px;top:166px"><div class="product-photo" role="img" aria-label="Product photo: white touch-screen kiosk"><span></span></div><p class="product-name">Verba vestra</p></div>
    <div class="product" style="left:0;top:332px"><div class="product-photo" role="img" aria-label="Product photo: white touch-screen kiosk"><span></span></div><p class="product-name">Nulla profecto est</p></div>
    <div class="product" style="left:216px;top:332px"><div class="product-photo" role="img" aria-label="Product photo: white touch-screen kiosk"><span></span></div><p class="product-name">Primo ad extremum</p></div>
    <div class="product" style="left:436px;top:332px"><div class="product-photo" role="img" aria-label="Product photo: white touch-screen kiosk"><span></span></div><p class="product-name">Neque enim civitas</p></div>
  </section>

  <div class="btn btn-back"><svg width="10" height="16" viewBox="0 0 10 16"><path d="M8 2 2 8l6 6" stroke="#fff" stroke-width="2" fill="none"/></svg>Back</div>
  <div class="btn btn-main">Main</div>
  <div class="btn btn-next">Next<svg width="10" height="16" viewBox="0 0 10 16"><path d="m2 2 6 6-6 6" stroke="#fff" stroke-width="2" fill="none"/></svg></div>

  <aside class="panel">
    <div class="panel-heading" style="top:26px"><span class="rule"></span><h2>Filters</h2><span class="rule"></span></div>
    <div class="select" style="top:70px">Num dixisset paulumque<svg width="20" height="12" viewBox="0 0 20 12"><path d="m2 2 8 8 8-8" stroke="#1f86e6" stroke-width="2.2" fill="none"/></svg></div>
    <div class="select" style="top:139px">Num dixisset paulumque<svg width="20" height="12" viewBox="0 0 20 12"><path d="m2 2 8 8 8-8" stroke="#1f86e6" stroke-width="2.2" fill="none"/></svg></div>
    <div class="panel-heading" style="top:216px"><span class="rule"></span><h2>Categories</h2><span class="rule"></span></div>

    <div class="category" style="left:24px;top:258px"><svg width="14" height="22" viewBox="0 0 14 22"><rect x="1" y="1" width="12" height="20" rx="2" fill="none" stroke="#1e88f0" stroke-width="2"/><circle cx="7" cy="17" r="1.2" fill="#1e88f0"/></svg>Mobile<br>Phones</div>
    <div class="category" style="left:134px;top:258px"><svg width="28" height="24" viewBox="0 0 24 22"><path fill="#1e88f0" d="M12 2 1 11h3v10h6v-6h4v6h6V11h3z"/></svg>Home<br>Decor</div>
    <div class="category" style="left:245px;top:258px"><svg width="22" height="24" viewBox="0 0 22 24"><path fill="#1e88f0" d="M2 1h2v7h1V1h2v7h1V1h2v9c0 1.5-1.2 2.5-2.5 2.5V23h-4V12.5C2.2 12.5 1 11.5 1 10V1zM14 1c4 0 6 3 6 8v5h-2v9h-4z"/></svg>Kitchen<br>Appliances</div>
    <div class="category" style="left:24px;top:370px"><svg width="14" height="22" viewBox="0 0 14 22"><rect x="1" y="1" width="12" height="20" rx="2" fill="none" stroke="#1e88f0" stroke-width="2"/><circle cx="7" cy="17" r="1.2" fill="#1e88f0"/></svg>Mobile<br>Phones</div>
    <div class="category" style="left:134px;top:370px"><svg width="28" height="24" viewBox="0 0 24 22"><path fill="#1e88f0" d="M12 2 1 11h3v10h6v-6h4v6h6V11h3z"/></svg>Home<br>Decor</div>
    <div class="category" style="left:245px;top:370px"><svg width="22" height="24" viewBox="0 0 22 24"><path fill="#1e88f0" d="M2 1h2v7h1V1h2v7h1V1h2v9c0 1.5-1.2 2.5-2.5 2.5V23h-4V12.5C2.2 12.5 1 11.5 1 10V1zM14 1c4 0 6 3 6 8v5h-2v9h-4z"/></svg>Kitchen<br>Appliances</div>
  </aside>

  <footer class="footer"><span>10:34, 03 of August 2017</span><span>Quicquid porro animo cernimus, id omne oritur a sensibus</span></footer>
</div>
</body>
</html>
```